Logo for Real Estate Company
Stationary and Business Cards
Simple
Glen Moravek
Broker
412 N. Calloway
Whitney, TX
moravekhomes@briskmail.example
www.moravekproperties.example

```html
<!DOCTYPE html>
<html lang="en">
<head>
<meta charset="utf-8">
<title>Moravek &amp; Associates Real Estate – Business Card</title>
<link rel="stylesheet" href="https://fonts.googleapis.com/css2?family=Arimo:wght@400;700&display=swap">
<style>
  :root{
    --bg:#d9dadc;
    --card:#ffffff;
    --blue:#1f6fb6;
    --blue-dark:#0f4f8f;
    --blue-light:#4aa3de;
    --green:#6cb33f;
    --sun:#f08a1c;
    --ink:#4a4a4a;
  }
  html,body{margin:0;padding:0;overflow:hidden;}
  body{
    width:1200px;height:901px;background:var(--bg);
    font-family:"Arimo",Arial,sans-serif;position:relative;
  }
  .card{
    position:absolute;width:600px;height:343px;background:var(--card);
    border-radius:16px;overflow:hidden;
    box-shadow:0 2px 6px rgba(0,0,0,.15);
  }
  .card-back{left:70px;top:70px;display:flex;align-items:center;justify-content:center;}
  .card-front{left:530px;top:488px;}

  .brand{display:flex;align-items:center;gap:10px;color:var(--blue);font-weight:700;}
  .brand-dot{border-radius:50%;background:var(--sun);flex:none;}
  .card-back .brand{font-size:34px;line-height:1.1;}
  .card-back .brand-dot{width:38px;height:38px;}

  .swoosh{position:absolute;inset:0;}
  .card-front .brand{position:absolute;left:36px;top:134px;font-size:19px;line-height:1.15;}
  .card-front .brand-dot{width:18px;height:18px;}

  .person{position:absolute;right:34px;top:96px;text-align:left;color:#fff;}
  .person-name{font-size:17px;font-weight:700;}
  .person-role{font-size:11px;margin-top:2px;opacity:.9;}

  .address{position:absolute;left:40px;top:232px;font-size:12px;color:var(--ink);line-height:1.45;}

  .contacts{position:absolute;left:340px;top:240px;list-style:none;margin:0;padding:0;font-size:12px;color:var(--ink);}
  .contacts li{display:flex;align-items:center;gap:8px;line-height:17px;}
  .contacts svg{width:11px;height:11px;fill:var(--blue-dark);flex:none;}
</style>
</head>
<body>

<section class="card card-back" aria-label="Card back">
  <div class="brand"><span class="brand-dot"></span><span>Moravek &amp; Associates<br>Real Estate</span></div>
</section>

<section class="card card-front" aria-label="Card front">
  <svg class="swoosh" viewBox="0 0 600 343" preserveAspectRatio="none" aria-hidden="true">
    <defs>
      <linearGradient id="bandGrad" x1="0" y1="0" x2="1" y2="1">
        <stop offset="0" stop-color="var(--blue-light)"/>
        <stop offset="0.6" stop-color="var(--blue)"/>
        <stop offset="1" stop-color="var(--blue-dark)"/>
      </linearGradient>
    </defs>
    <path d="M0,0 H600 V300 C520,170 300,60 0,42 Z" fill="url(#bandGrad)"/>
    <path d="M0,52 C300,72 520,180 600,312" fill="none" stroke="var(--green)" stroke-width="9"/>
  </svg>

  <div class="brand"><span class="brand-dot"></span><span>Moravek &amp; Associates<br>Real Estate</span></div>

  <div class="person">
    <div class="person-name">Glen Moravek</div>
    <div class="person-role">Broker</div>
  </div>

  <div class="address">412 N. Calloway Whitney,<br>TX 76692</div>

  <ul class="contacts">
    <li><svg viewBox="0 0 12 12"><path d="M3 1l2 2-1 1.5c.7 1.4 1.8 2.5 3.2 3.2L8.7 6.7l2 2-1.2 1.8C5.5 10.3 1.7 6.5 1.5 2.5z"/></svg>254-555-0123</li>
    <li><svg viewBox="0 0 12 12"><rect x="3" y="0.5" width="6" height="11" rx="1"/></svg>254-555-0303</li>
    <li><svg viewBox="0 0 12 12"><rect x="1" y="4" width="10" height="6" rx="1"/><rect x="3" y="1" width="6" height="3"/></svg>254-555-0096</li>
    <li><svg viewBox="0 0 12 12"><path d="M1 2.5h10v7H1z M1 2.5l5 4 5-4" stroke="#fff" stroke-width="0.8"/></svg>moravekhomes@briskmail.example</li>
    <li><svg viewBox="0 0 12 12"><circle cx="6" cy="6" r="5"/></svg>www.moravekproperties.example</li>
  </ul>
</section>

</body>
</html>
```